Onboarding Carousel UI/UX design

We need a great UI/UX design for our onboarding carousel as attached in the PDF document. The chosen designers will be given our brand book with colors and styles to be used. The images must be focused on the content of each slide and be professional unique style (Do not use the childish cartoons we have used for placeholders)

Industry/Entity Type

Mortgage Brokerage

Number of Pages Required

5+ page

Other font styles liked:
• Roboto

Requirements
Must have
• Great UI / UX design
Very relevant content of the images to match the slide
Nice to have
• Brand book

https://proto.velmarink.com/view/a4c7e210-8b3f-4d19-a6e2-5f0c91b7d3e8-c2fa/?fullscreen

Image styles we like. Would need to be customized and made unique for us.

https://pixelmarsh.com/shots/4817302-Tarvo-Quillnet-Illustration-Collaboration
https://brackwellstudio.co.za/software-client-style-frames
Should not have
• Do not use the childish images we have used as placeholders

```html
<!DOCTYPE html>
<html lang="en">
<head>
<meta charset="utf-8">
<title>Onboarding Carousel</title>
<link rel="stylesheet" href="https://fonts.googleapis.com/css2?family=Roboto:wght@400;500;700&display=swap">
<style>
  :root {
    --canvas: #e8e8e8;
    --screen: #ffffff;
    --title: #1b4e8d;
    --body: #2f2f2f;
    --muted: #777777;
    --dot: #cacaca;
    --dot-active: #e5007d;
    --action: #7f9a0c;
    --link: #1b4e8d;
    --ink: #222222;
  }
  * { box-sizing: border-box; margin: 0; padding: 0; }
  html, body { width: 734px; height: 1200px; overflow: hidden; }
  body {
    background: var(--canvas);
    font-family: "Roboto", Arial, sans-serif;
    position: relative;
  }
  .screen {
    position: absolute;
    width: 224px;
    height: 486px;
    background: var(--screen);
    border-radius: 22px;
    overflow: hidden;
    box-shadow: 0 2px 10px rgba(0,0,0,0.08);
  }
  .screen--welcome  { left: 94px;  top: 76px; }
  .screen--account  { left: 418px; top: 76px; }
  .screen--secure   { left: 94px;  top: 646px; }
  .screen--identity { left: 418px; top: 646px; }

  .status-bar {
    position: absolute; top: 10px; left: 14px; right: 14px;
    display: flex; justify-content: space-between;
    font-size: 7px; color: var(--ink);
  }
  .art {
    position: absolute; top: 44px; left: 20px;
    width: 184px; height: 156px;
    border-radius: 10px;
  }
  .art--desk     { background: linear-gradient(160deg, #f4efe8 0%, #e3dcd2 55%, #c8d8b4 100%); }
  .art--mail     { background: linear-gradient(150deg, #eaf1fb 0%, #f6e2a8 45%, #9ed2d8 100%); }
  .art--phone    { background: linear-gradient(160deg, #e6f3fa 0%, #8fcbe8 50%, #f3c64f 100%); }
  .art--verify   { background: linear-gradient(160deg, #eef5fb 0%, #b9d7ef 55%, #f19a6c 100%); }

  .copy {
    position: absolute; left: 10px; right: 10px; top: 224px;
    text-align: center;
  }
  .screen--account .copy,
  .screen--secure .copy,
  .screen--identity .copy { top: 228px; }
  .copy__title {
    color: var(--title);
    font-weight: 500;
    font-size: 17.5px;
    line-height: 21.5px;
    margin-bottom: 11px;
  }
  .copy__lead {
    color: var(--body);
    font-size: 10.6px;
    line-height: 16.5px;
    letter-spacing: 0.1px;
    margin-bottom: 9px;
  }
  .copy__note {
    color: var(--muted);
    font-size: 8.2px;
    line-height: 15px;
  }
  .copy__note + .copy__note { margin-top: 3px; }

  .pager {
    position: absolute; top: 402px; left: 0; right: 0;
    display: flex; justify-content: center; gap: 4.4px;
  }
  .pager__dot {
    width: 6.5px; height: 6.5px; border-radius: 50%;
    background: var(--dot);
  }
  .pager__dot--active { background: var(--dot-active); }

  .next-button {
    position: absolute; top: 428px; right: 22px;
    width: 45px; height: 18px;
    background: var(--action);
    color: #fff;
    font-size: 8.5px; font-weight: 700;
    display: flex; align-items: center; justify-content: center;
    letter-spacing: 0.3px;
  }
  .account-prompt {
    position: absolute; top: 430px; left: 21px;
    font-size: 8px; color: var(--ink); line-height: 10px;
  }
  .account-prompt__link { display: block; color: var(--link); font-size: 6.5px; font-weight: 500; }

  .nav-bar {
    position: absolute; top: 466px; left: 12px; right: 12px;
    display: flex; justify-content: space-between; align-items: center;
  }
</style>
</head>
<body>

<section class="screen screen--welcome">
  <div class="status-bar"><span>08:31</span><span>99%</span></div>
  <div class="art art--desk" role="img" aria-label="Illustration of a broker working at a laptop on a desk next to a potted plant"></div>
  <div class="copy">
    <h1 class="copy__title">Welcome to<br>Meridane Brokers<br>Apply Online</h1>
    <p class="copy__lead">You can apply online for your<br>next mortgage credit in about<br>20 minutes.</p>
    <p class="copy__note">It's easy, and we will guide you all the way.</p>
    <p class="copy__note">See the five simple steps that you have to take!</p>
  </div>
  <div class="pager">
    <span class="pager__dot pager__dot--active"></span><span class="pager__dot"></span><span class="pager__dot"></span><span class="pager__dot"></span><span class="pager__dot"></span><span class="pager__dot"></span><span class="pager__dot"></span>
  </div>
  <div class="account-prompt">Already have an account?<span class="account-prompt__link">Logon</span></div>
  <div class="next-button">NEXT</div>
  <div class="nav-bar">
    <svg width="8" height="8" viewBox="0 0 8 8"><g fill="#222"><rect x="1" y="1" width="1.2" height="6"/><rect x="3.4" y="1" width="1.2" height="6"/><rect x="5.8" y="1" width="1.2" height="6"/></g></svg>
    <svg width="8" height="8" viewBox="0 0 8 8"><rect x="1" y="1" width="6" height="6" rx="1.2" fill="none" stroke="#222" stroke-width="1"/></svg>
    <svg width="8" height="8" viewBox="0 0 8 8"><path d="M5.5 1.5 3 4l2.5 2.5" fill="none" stroke="#222" stroke-width="1"/></svg>
  </div>
</section>

<section class="screen screen--account">
  <div class="status-bar"><span>08:31</span><span>99%</span></div>
  <div class="art art--mail" role="img" aria-label="Illustration of a large phone with a megaphone, envelopes and small people creating an account"></div>
  <div class="copy">
    <h2 class="copy__title">#1 Create Your<br>Personal Account</h2>
    <p class="copy__lead">You will need a valid email<br>address to create your account</p>
    <p class="copy__note">We will send you a confirmation email, make<br>sure you click the link to verify your<br>email address.</p>
  </div>
  <div class="pager">
    <span class="pager__dot"></span><span class="pager__dot pager__dot--active"></span><span class="pager__dot"></span><span class="pager__dot"></span><span class="pager__dot"></span><span class="pager__dot"></span><span class="pager__dot"></span>
  </div>
  <div class="next-button">NEXT</div>
  <div class="nav-bar">
    <svg width="8" height="8" viewBox="0 0 8 8"><g fill="#222"><rect x="1" y="1" width="1.2" height="6"/><rect x="3.4" y="1" width="1.2" height="6"/><rect x="5.8" y="1" width="1.2" height="6"/></g></svg>
    <svg width="8" height="8" viewBox="0 0 8 8"><rect x="1" y="1" width="6" height="6" rx="1.2" fill="none" stroke="#222" stroke-width="1"/></svg>
    <svg width="8" height="8" viewBox="0 0 8 8"><path d="M5.5 1.5 3 4l2.5 2.5" fill="none" stroke="#222" stroke-width="1"/></svg>
  </div>
</section>

<section class="screen screen--secure">
  <div class="status-bar"><span>08:31</span><span>99%</span></div>
  <div class="art art--phone" role="img" aria-label="Illustration of a mobile phone login screen with a padlock, a key and people securing the account"></div>
  <div class="copy">
    <h2 class="copy__title">#2 Secure your account<br>with your mobile phone</h2>
    <p class="copy__lead">You will need a valid mobile phone<br>number to enable two factor<br>authentication.</p>
    <p class="copy__note">We will send you an SMS containing<br>a security code to verify your mobile number.</p>
  </div>
  <div class="pager">
    <span class="pager__dot"></span><span class="pager__dot"></span><span class="pager__dot pager__dot--active"></span><span class="pager__dot"></span><span class="pager__dot"></span><span class="pager__dot"></span><span class="pager__dot"></span>
  </div>
  <div class="next-button">NEXT</div>
  <div class="nav-bar">
    <svg width="8" height="8" viewBox="0 0 8 8"><g fill="#222"><rect x="1" y="1" width="1.2" height="6"/><rect x="3.4" y="1" width="1.2" height="6"/><rect x="5.8" y="1" width="1.2" height="6"/></g></svg>
    <svg width="8" height="8" viewBox="0 0 8 8"><rect x="1" y="1" width="6" height="6" rx="1.2" fill="none" stroke="#222" stroke-width="1"/></svg>
    <svg width="8" height="8" viewBox="0 0 8 8"><path d="M5.5 1.5 3 4l2.5 2.5" fill="none" stroke="#222" stroke-width="1"/></svg>
  </div>
</section>

<section class="screen screen--identity">
  <div class="status-bar"><span>08:31</span><span>99%</span></div>
  <div class="art art--verify" role="img" aria-label="Illustration of a desktop monitor with a security shield, ID cards, documents and a magnifier for identity verification"></div>
  <div class="copy">
    <h2 class="copy__title">#3 Verify Your Identity<br>Online</h2>
    <p class="copy__lead">You will need to have a valid Romanian<br>ID card or residence permit</p>
    <p class="copy__note">From your smart phone, you will take<br>a photo of your card and make a<br>selfie video.</p>
  </div>
  <div class="pager">
    <span class="pager__dot"></span><span class="pager__dot"></span><span class="pager__dot"></span><span class="pager__dot pager__dot--active"></span><span class="pager__dot"></span><span class="pager__dot"></span><span class="pager__dot"></span>
  </div>
  <div class="next-button">NEXT</div>
  <div class="nav-bar">
    <svg width="8" height="8" viewBox="0 0 8 8"><g fill="#222"><rect x="1" y="1" width="1.2" height="6"/><rect x="3.4" y="1" width="1.2" height="6"/><rect x="5.8" y="1" width="1.2" height="6"/></g></svg>
    <svg width="8" height="8" viewBox="0 0 8 8"><rect x="1" y="1" width="6" height="6" rx="1.2" fill="none" stroke="#222" stroke-width="1"/></svg>
    <svg width="8" height="8" viewBox="0 0 8 8"><path d="M5.5 1.5 3 4l2.5 2.5" fill="none" stroke="#222" stroke-width="1"/></svg>
  </div>
</section>

</body>
</html>
```